Business Card Design Project

Roofing Consultant firm needs business card design

R.T. Haverbrook & Co., Inc
Roofing Consultants and Contractors
Specializing in Construction Defect Litigation

4817 Willow Crest Ln.
San Diego, CA 92847
Licences:
CA 514728, AZ 907465, NV 0063512
www.rthaverbrook-example.com

Will need cards for 3 persons:
Robert T. Haverbrook - Principal Consultant
Kevin Sallow - Associate Expert
Marla Vinsett - Controller
ph-555-217-6400
fax -555-217-6402
Cell - (will be 3 different numbers)
Email - (will be 3 different addresses)
Attached graphic is what we had before..the RTH with the roof graphic has been our logo for awhile, but we are open to change.
Updates

I now see we will need to add an email field to the design.  Sorry I didnt think of it when I was setting this up.  Thank you for your submittals. They are all very good. 

Target Market(s)

Attorneys, Homeowner Associations, Insurance Carriers

Industry/Entity Type

Business

Requirements
Must have
• RTH logo roof design. (owner created)

```html
<!DOCTYPE html>
<html lang="en">
<head>
<meta charset="utf-8">
<title>R.T. Haverbrook &amp; Co., Inc – Business Card</title>
<link rel="stylesheet" href="https://fonts.googleapis.com/css2?family=Arimo:wght@700&family=Michroma&display=swap">
<style>
  :root {
    --backdrop: #3b3b3d;
    --card-top: #053478;
    --card-bottom: #0a2a5c;
    --accent: #1aa0e6;
    --band-top: #3fb4ef;
    --band-bottom: #0b6fb8;
    --white: #ffffff;
    --divider: #2a5aa0;
  }
  * { margin: 0; padding: 0; box-sizing: border-box; }
  html, body { width: 1200px; height: 900px; overflow: hidden; }
  body { background: var(--backdrop); position: relative; }

  .card {
    position: absolute;
    top: 293px;
    width: 513px;
    height: 314px;
    border-radius: 28px;
    background: linear-gradient(180deg, var(--card-top) 0%, var(--card-bottom) 100%);
    overflow: hidden;
    color: var(--white);
  }
  .card--front { left: 73px; }
  .card--back { left: 616px; }

  /* Brand block */
  .brand { position: absolute; }
  .brand__name {
    font-family: "Arimo", Arial, sans-serif;
    font-weight: 700;
    color: var(--accent);
    line-height: 1.05;
    text-transform: uppercase;
    text-align: right;
    white-space: nowrap;
  }
  .brand__rule { height: 2px; background: var(--white); }
  .brand__tagline {
    font-family: "Arimo", Arial, sans-serif;
    font-weight: 700;
    text-transform: uppercase;
    color: var(--white);
    white-space: nowrap;
  }

  .card--front .brand { left: 128px; top: 168px; width: 266px; }
  .card--front .brand__name { font-size: 22px; letter-spacing: 0.3px; margin-bottom: 8px; }
  .card--front .brand__rule { margin-bottom: 8px; }
  .card--front .brand__tagline { font-size: 10.6px; letter-spacing: 0.1px; }

  .card--back .brand { left: 28px; top: 150px; width: 178px; }
  .card--back .brand__name { font-size: 14.5px; margin-bottom: 5px; }
  .card--back .brand__rule { margin-bottom: 5px; height: 1.5px; }
  .card--back .brand__tagline { font-size: 7.1px; }

  .divider {
    position: absolute;
    left: 237px; top: 56px;
    width: 1px; height: 186px;
    background: var(--divider);
  }

  .contact {
    position: absolute;
    left: 268px; top: 58px;
    font-family: "Michroma", "Eurostile", sans-serif;
    font-variant: small-caps;
    letter-spacing: 1px;
    white-space: nowrap;
  }
  .contact__name { color: var(--accent); font-size: 12px; line-height: 18px; }
  .contact__title { color: var(--white); font-size: 10px; line-height: 16px; }
  .contact__group { margin-top: 16px; }
  .contact__line {
    display: flex; align-items: center;
    font-size: 10px; line-height: 16px; color: var(--white);
    white-space: nowrap;
  }
  .contact__line--compact { font-size: 8.2px; letter-spacing: 0.4px; }
  .contact__line--indent { padding-left: 17px; }
  .contact__line svg { width: 11px; height: 11px; margin-right: 6px; flex: none; fill: var(--accent); }

  .licence-band {
    position: absolute;
    left: 0; right: 0; top: 268px; height: 24px;
    background: linear-gradient(180deg, var(--band-top) 0%, var(--band-bottom) 100%);
    font-family: "Michroma", "Eurostile", sans-serif;
    font-variant: small-caps;
    font-size: 7.5px; letter-spacing: 0.8px;
    color: var(--white);
    text-align: center;
    line-height: 24px;
    white-space: nowrap;
  }
</style>
</head>
<body>

<section class="card card--front" aria-label="Card front">
  <div class="brand">
    <p class="brand__name">R.T. Haverbrook<br>&amp; Co., Inc</p>
    <div class="brand__rule"></div>
    <p class="brand__tagline">Roofing Consultants and Contractors</p>
  </div>
</section>

<section class="card card--back" aria-label="Card back">
  <div class="brand">
    <p class="brand__name">R.T. Haverbrook<br>&amp; Co., Inc</p>
    <div class="brand__rule"></div>
    <p class="brand__tagline">Roofing Consultants and Contractors</p>
  </div>

  <div class="divider"></div>

  <div class="contact">
    <p class="contact__name">Robert T. Haverbrook</p>
    <p class="contact__title">Principal Consultant</p>

    <div class="contact__group">
      <p class="contact__line">
        <svg viewBox="0 0 12 12" aria-hidden="true"><path d="M6 0a4 4 0 0 0-4 4c0 3 4 8 4 8s4-5 4-8a4 4 0 0 0-4-4zm0 5.6A1.6 1.6 0 1 1 6 2.4a1.6 1.6 0 0 1 0 3.2z"/></svg>
        4817 Willow Crest Ln.
      </p>
      <p class="contact__line contact__line--indent">San Diego, CA 92847</p>
    </div>

    <div class="contact__group">
      <p class="contact__line">
        <svg viewBox="0 0 12 12" aria-hidden="true"><path d="M2.5 1l2 2-1 1.5a7 7 0 0 0 4 4L9 7.5l2 2L9.5 11C5 11 1 7 1 2.5z"/></svg>
        555 217 6400
      </p>
      <p class="contact__line">
        <svg viewBox="0 0 12 12" aria-hidden="true"><path d="M3 1h5v3H3zM1 5h10v5H9V8H3v2H1zM3 9h6v2H3z"/></svg>
        555 217 6402
      </p>
      <p class="contact__line">
        <svg viewBox="0 0 12 12" aria-hidden="true"><path d="M3.5 0h5a1 1 0 0 1 1 1v10a1 1 0 0 1-1 1h-5a1 1 0 0 1-1-1V1a1 1 0 0 1 1-1zm.5 1.5v8h4v-8z"/></svg>
        555 217 6488
      </p>
      <p class="contact__line contact__line--compact">
        <svg viewBox="0 0 12 12" aria-hidden="true"><path d="M0 2.5h12v1L6 7 0 3.5zM0 5l6 3.5L12 5v5H0z"/></svg>
        info@rthaverbrook-example.com
      </p>
      <p class="contact__line contact__line--compact">
        <svg viewBox="0 0 12 12" aria-hidden="true"><path d="M6 0a6 6 0 1 0 0 12A6 6 0 0 0 6 0zm0 1c.8.8 1.4 2.3 1.5 4.5h-3C4.6 3.3 5.2 1.8 6 1zM1 6.5h2.5c.1 1.7.5 3.2 1.1 4.3A5 5 0 0 1 1 6.5zm0-1a5 5 0 0 1 3.6-4.3C4 2.3 3.6 3.8 3.5 5.5zm5 5.5c-.8-.8-1.4-2.3-1.5-4.5h3c-.1 2.2-.7 3.7-1.5 4.5zm1.4-.2c.6-1.1 1-2.6 1.1-4.3H11a5 5 0 0 1-3.6 4.3zM8.5 5.5c-.1-1.7-.5-3.2-1.1-4.3A5 5 0 0 1 11 5.5z"/></svg>
        www.rthaverbrook-example.com
      </p>
    </div>
  </div>

  <p class="licence-band">Licences: CA 514728, AZ 907465, NV 0063512</p>
</section>

</body>
</html>
```